Vurlo App

We want to have a web banner (4-5 slides) flash or whatever.
We are innovative next generation messenger with a good design, themes, snap mode, pinging and other features.
Inspired by night, by techno music, by energy, by innovations and next generation.
High tech.

The name of the app : Vurlo
vurloapp.example

The banner will be used for nightdeckmag.example

We want the banner to be creative, and deliver the inspiration of the app.

All the assets, logos and so on can me delivered to you via email by request.

```html
<!DOCTYPE html>
<html lang="en">
<head>
<meta charset="utf-8">
<title>Vurlo App – web banner</title>
<link rel="stylesheet" href="https://fonts.googleapis.com/css2?family=Roboto+Condensed:wght@700&display=swap">
<style>
  :root {
    --banner-bg: #3d3d3d;
    --text-light: #ffffff;
    --accent-blue: #5cc3f2;
  }
  html, body {
    margin: 0;
    padding: 0;
    width: 1200px;
    height: 148px;
    overflow: hidden;
    background: var(--banner-bg);
  }
  .banner {
    position: relative;
    width: 1200px;
    height: 148px;
    background: var(--banner-bg);
    font-family: "Roboto Condensed", "Arial Narrow", sans-serif;
    font-weight: 700;
    color: var(--text-light);
  }
  .hashtag {
    position: absolute;
    top: 40px;
    margin: 0;
    font-size: 52px;
    line-height: 64px;
    letter-spacing: -0.5px;
  }
  .hashtag--nextgen { left: 219px; }
  .hashtag--app { left: 527px; }
  .brand {
    position: absolute;
    top: 42px;
    left: 960px;
    display: flex;
    align-items: center;
    gap: 18px;
  }
  .brand__mark {
    width: 54px;
    height: 54px;
    background: var(--accent-blue);
    border-radius: 4px;
  }
  .brand__name {
    font-size: 44px;
    line-height: 54px;
    letter-spacing: -0.5px;
  }
</style>
</head>
<body>
  <div class="banner">
    <p class="hashtag hashtag--nextgen">#nextgen</p>
    <p class="hashtag hashtag--app">#vurloapp</p>
    <div class="brand">
      <span class="brand__mark" aria-hidden="true"></span>
      <span class="brand__name">vurlo</span>
    </div>
  </div>
</body>
</html>
```